Business Cards Brimsworth Nuptials

I have a new webpage address and would like to update my business cards with Facebook and Instagram links as well. I need assistance with designing it. I have attached an old business card.

Target Market(s)

Potential couples wanting to get married and vendors who work with weddings

Industry/Entity Type

Wedding

Contact Information for Business Card

Name of Company (Brimsworth Nuptials), Pam Holcroft, Phone number (480-762-3038), Webpage: www.brimsworthnuptials4u.example, Facebook Link: Brimsworth Nuptials, Instagram Link: BrimsworthNuptials4u

Colors
0094D4
00A9DD
6FCCEA
C7EBF8
E9F6FB
00AB8E
00BBA5
67D7C9
C6EFE9
E9F9F6

Requirements
Nice to have
• Florals with teal on back of card. Not sure what needs to be on front and what on back
Should not have
• Definitive man/woman couple

```html
<!DOCTYPE html>
<html lang="en">
<head>
<meta charset="utf-8">
<title>Brimsworth Nuptials – Business Card</title>
<link rel="stylesheet" href="https://fonts.googleapis.com/css2?family=Bodoni+Moda:opsz,wght@6..96,400;6..96,700;6..96,800&display=swap">
<style>
  :root {
    --brand-teal: #2fc49c;
    --ink: #111111;
    --paper: #ffffff;
    --frame: #1a1a1a;
    --floral-light: #f4f6f6;
    --floral-mid: #e3e8e7;
  }
  * { box-sizing: border-box; margin: 0; padding: 0; }
  html, body {
    width: 1200px;
    height: 686px;
    overflow: hidden;
    background: var(--paper);
  }
  .card {
    position: relative;
    width: 1200px;
    height: 686px;
    background: var(--paper);
    border: 1.5px solid var(--frame);
    font-family: "Bodoni Moda", "Didot", serif;
    color: var(--ink);
    overflow: hidden;
  }
  .floral-art {
    position: absolute;
    right: 0;
    top: 30px;
    width: 470px;
    height: 656px;
  }
  .company-name {
    position: absolute;
    left: 100px;
    top: 80px;
    width: 500px;
    text-align: center;
    color: var(--brand-teal);
    font-weight: 800;
    font-size: 80px;
    line-height: 1.08;
    letter-spacing: -0.5px;
  }
  .company-name span { display: block; }
  .contact-name {
    position: absolute;
    left: 185px;
    top: 322px;
    font-weight: 800;
    font-size: 43px;
    line-height: 1;
  }
  .contact-list {
    position: absolute;
    left: 117px;
    top: 388px;
    list-style: none;
  }
  .contact-item {
    display: flex;
    align-items: center;
    height: 58px;
    font-size: 37px;
    font-weight: 400;
  }
  .contact-icon {
    width: 52px;
    height: 52px;
    margin-right: 16px;
    flex: none;
  }
</style>
</head>
<body>
  <main class="card">
    <svg class="floral-art" role="img" aria-label="Line-art illustration of daffodils with long leaves" viewBox="0 0 470 656" preserveAspectRatio="none">
      <defs>
        <radialGradient id="floralWash" cx="0.65" cy="0.45" r="0.7">
          <stop offset="0" stop-color="var(--floral-mid)"/>
          <stop offset="0.6" stop-color="var(--floral-light)"/>
          <stop offset="1" stop-color="#ffffff"/>
        </radialGradient>
      </defs>
      <rect width="470" height="656" fill="url(#floralWash)"/>
    </svg>

    <h1 class="company-name">
      <span>Brimsworth</span>
      <span>Nuptials</span>
    </h1>

    <p class="contact-name">Pam Holcroft</p>

    <ul class="contact-list">
      <li class="contact-item">
        <svg class="contact-icon" viewBox="0 0 52 52" aria-hidden="true">
          <circle cx="26" cy="26" r="23" fill="none" stroke="var(--brand-teal)" stroke-width="2"/>
          <path d="M19 15c1.5-1 3-.8 3.8.6l2 3.6c.6 1.1.3 2.3-.7 3l-1.4 1c1 2.6 3 4.7 5.6 5.8l1-1.4c.7-1 2-1.3 3-.7l3.6 2c1.4.8 1.6 2.4.6 3.8l-1.3 1.6c-1 1.2-2.6 1.7-4.1 1.2C23.8 37 16 29.2 14.6 21.8c-.4-1.5.1-3 1.3-4z" fill="var(--brand-teal)"/>
        </svg>
        <span>480-762-3038</span>
      </li>
      <li class="contact-item">
        <svg class="contact-icon" viewBox="0 0 52 52" aria-hidden="true">
          <circle cx="26" cy="26" r="23" fill="none" stroke="var(--brand-teal)" stroke-width="2"/>
        </svg>
        <span>BrimsworthNuptials</span>
      </li>
      <li class="contact-item">
        <svg class="contact-icon" viewBox="0 0 52 52" aria-hidden="true">
          <circle cx="26" cy="26" r="23" fill="none" stroke="var(--brand-teal)" stroke-width="2"/>
        </svg>
        <span>BrimsworthNuptials4u</span>
      </li>
      <li class="contact-item">
        <svg class="contact-icon" viewBox="0 0 52 52" aria-hidden="true">
          <circle cx="26" cy="26" r="23" fill="none" stroke="var(--brand-teal)" stroke-width="2"/>
        </svg>
        <span>www.brimsworthnuptials4u.example</span>
      </li>
    </ul>
  </main>
</body>
</html>
```